Ember needs a new design we have an updated logo and want a high qualitative high end feel

feel and aesthetic should be high qualitative like the packaging in a zelvo or the qualatative weight/feel of an zelvo design. modern, elegant bold.probably just the ember logo on the backone vesion could be blue background white letter ... open to ideas
legal, insurance , medical, finance vantor 300
Information Technology
Serif

```html
<!DOCTYPE html>
<html lang="en">
<head>
<meta charset="UTF-8">
<title>Ember — Business Card</title>
<link href="https://fonts.googleapis.com/css2?family=Montserrat:wght@400;500;600&display=swap" rel="stylesheet">
<style>
  :root {
    --stage: #262626;
    --card-dark: #1b2b40;
    --card-light: #2b3f55;
    --ink: #ffffff;
    --rule: rgba(255,255,255,0.75);
  }
  * { margin: 0; padding: 0; box-sizing: border-box; }
  html, body { width: 1200px; height: 900px; overflow: hidden; background: var(--stage); }
  body {
    font-family: "Montserrat", sans-serif;
    color: var(--ink);
    display: flex; flex-direction: column; align-items: center; justify-content: center;
    gap: 40px;
  }
  .card {
    width: 665px; height: 380px;
    background: linear-gradient(135deg, var(--card-dark) 0%, var(--card-dark) 45%, var(--card-light) 100%);
    position: relative;
  }
  .brand { display: flex; align-items: center; gap: 10px; }
  .brand-name { font-weight: 500; font-size: 86px; letter-spacing: 1px; line-height: 1; }
  .brand-dot { width: 12px; height: 12px; border-radius: 50%; background: var(--ink); align-self: flex-start; margin-top: 14px; }
  .card-front { display: flex; align-items: center; justify-content: center; }
  .card-back { display: flex; align-items: center; padding-left: 50px; }
  .card-back .brand-name { font-size: 72px; }
  .divider { width: 1px; height: 210px; background: var(--rule); margin: 0 36px 0 42px; }
  .contact { display: flex; flex-direction: column; }
  .person-name { font-weight: 600; font-size: 25px; letter-spacing: 2px; text-transform: uppercase; }
  .person-role { font-size: 19px; margin-top: 2px; }
  .address { font-size: 19px; line-height: 1.3; margin-top: 16px; letter-spacing: .5px; }
  .links { list-style: none; margin-top: 12px; font-size: 19px; line-height: 1.35; letter-spacing: .5px; }
  .links li { display: flex; align-items: center; gap: 10px; }
  .links svg { width: 13px; height: 13px; flex: none; }
  .web strong { font-weight: 600; }
</style>
</head>
<body>
  <section class="card card-front">
    <div class="brand"><span class="brand-name">ember</span><span class="brand-dot"></span></div>
  </section>

  <section class="card card-back">
    <div class="brand"><span class="brand-name">ember</span><span class="brand-dot"></span></div>
    <div class="divider"></div>
    <div class="contact">
      <p class="person-name">Daniel Hart</p>
      <p class="person-role">Director</p>
      <p class="address">2417 W Main St Suite 305<br>Lakeview, VA 23104</p>
      <ul class="links">
        <li><svg viewBox="0 0 16 16" fill="none" stroke="#fff" stroke-width="1.6"><path d="M4 1.5l2.5 3-1.5 2a8 8 0 0 0 4.5 4.5l2-1.5 3 2.5-1.5 2.5C7 14 2 9 1.5 3z"/></svg>555 214-0800</li>
        <li><svg viewBox="0 0 16 16" fill="none" stroke="#fff" stroke-width="1.6"><rect x="1.5" y="3.5" width="13" height="9"/><path d="M1.5 3.5l6.5 5 6.5-5"/></svg>help@embermsg.com</li>
        <li class="web"><svg viewBox="0 0 16 16" fill="none" stroke="#fff" stroke-width="1.3"><circle cx="8" cy="8" r="6.5"/><ellipse cx="8" cy="8" rx="3" ry="6.5"/><path d="M1.5 8h13M2.5 5h11M2.5 11h11"/></svg><span>www.<strong>embermsg</strong>.com</span></li>
      </ul>
    </div>
  </section>
</body>
</html>
```